Banner Ads for Online Poker Promotion

We are an online poker network, the KRX (www.thekrx.eu). We are looking for a small selection of web banner ads for our latest promotion and we are trying crowdsourcing for the first time!

Banner sizes that we need are:
- 196x523 (static .psd and .png)
- 199x129 (static .psd and .png)
- 447x426 (static .psd and .png)
- 500x400 (static .psd and .png)
- 697x167 (static .psd and .png)
- 460x60 (animated .gif)

The promotion name is ‘Late Rush’ and the concept is that a person who enters one of the specified tournaments four or more times during the promotion will win a free ticket to play that tournament again. So effectively a ‘Rush Late, Bag a Seat’ promo. We also are giving away €10,000 in free entries to the tournaments during the promotion. The specific tournaments are called ‘Calm Dawn Out’ and ‘The Sun Deck’ and run daily on our network. The promotion runs October 1 – 31.

Guidelines:

The name of the promotion, ‘Late Rush’, should feature prominently in the banners.

The strap line can be ‘Rush Late, Bag a Seat’ or something that encourages players to ‘take a shot’ at the tournaments.

Our network logo may feature, but is not absolutely necessary.

Examples of past promotional imagery can be found on our website, in particular these pages: http://www.thekrx.eu/promotions/ and http://www.thekrx.eu/promotions/archived-promotions/

We are looking to go in a more modern and risqué direction than the past, in order to stand out from competition which is very bland.

Please do not use common poker imagery – so no cards, chips, suit icons etc – or objects associated with live poker (tables, etc). This sort of imagery is too clichéd.

More like iOS7, less like iOS6

Think glamour, neon, rock music, extreme sports, and the Soft Tide!

If any further guidance is needed please don’t hesitate to ask.

```html
<!DOCTYPE html>
<html lang="en">
<head>
<meta charset="utf-8">
<title>Late Rush – Banner Set</title>
<link rel="stylesheet" href="https://fonts.googleapis.com/css2?family=Lato:wght@400;700;900&family=Metal+Mania&display=swap">
<style>
  :root {
    --stage: #dcdcdd;
    --banner-dark: #1c1c1d;
    --banner-mid: #3a1214;
    --ray-red: #8a1116;
    --title-red: #c8141b;
    --title-glow: #ff2a22;
    --button-red: #d4141a;
    --button-dark: #9c0c10;
    --text-white: #ffffff;
    --amount-silver: #e9edf2;
  }
  * { margin: 0; padding: 0; box-sizing: border-box; }
  html, body { width: 1200px; height: 857px; overflow: hidden; }
  body {
    background: var(--stage);
    font-family: "Lato", sans-serif;
    color: var(--text-white);
    position: relative;
  }
  .banner {
    position: absolute;
    overflow: hidden;
    background: radial-gradient(ellipse at 50% 55%, var(--ray-red) 0%, var(--banner-mid) 45%, var(--banner-dark) 85%);
  }
  .banner-art { position: absolute; inset: 0; }
  .banner > *:not(.banner-art) { position: absolute; }

  .prize-amount {
    font-weight: 900;
    color: var(--amount-silver);
    text-shadow: 0 2px 3px rgba(0,0,0,.8);
    letter-spacing: -0.5px;
    white-space: nowrap;
  }
  .prize-note { font-size: 12px; letter-spacing: .6px; white-space: nowrap; }
  .promo-title {
    font-family: "Metal Mania", cursive;
    color: var(--title-red);
    -webkit-text-stroke: 2px #0c0000;
    text-shadow: 0 0 12px var(--title-glow), 0 0 24px rgba(255,40,30,.6);
    white-space: nowrap;
    text-align: center;
    line-height: 1;
  }
  .tagline {
    letter-spacing: 1px;
    white-space: nowrap;
    text-shadow: 0 2px 6px rgba(0,0,0,.9);
    text-align: center;
  }
  .tagline strong { font-weight: 900; }
  .promo-dates { font-size: 15px; letter-spacing: .4px; white-space: nowrap; }
  .try-now {
    background: linear-gradient(180deg, var(--button-red), var(--button-dark));
    clip-path: polygon(8% 0, 100% 0, 100% 100%, 0 100%);
    font-weight: 700;
    display: flex; align-items: center; justify-content: center; gap: 8px;
  }
  .try-now svg { width: 10px; height: 12px; }
  .network-name { font-size: 22px; font-weight: 400; letter-spacing: 1px; display: flex; align-items: center; gap: 6px; }
  .network-name span.mark { width: 10px; height: 10px; background: var(--text-white); display: inline-block; }

  /* 697 x 167 */
  .banner-leaderboard { left: 52px; top: 64px; width: 697px; height: 167px; }
  .banner-leaderboard .prize-amount { left: 14px; top: 8px; font-size: 32px; }
  .banner-leaderboard .prize-note { left: 18px; top: 50px; }
  .banner-leaderboard .network-name { left: 20px; top: 128px; }
  .banner-leaderboard .promo-title { left: 160px; width: 360px; top: 14px; font-size: 78px; }
  .banner-leaderboard .tagline { left: 160px; width: 360px; top: 128px; font-size: 18px; }
  .banner-leaderboard .promo-dates { right: 14px; top: 16px; }
  .banner-leaderboard .try-now { right: 0; bottom: 0; width: 130px; height: 34px; font-size: 16px; }

  /* 199 x 129 */
  .banner-small { left: 781px; top: 67px; width: 199px; height: 129px; }
  .banner-small .prize-amount { left: 12px; top: 4px; font-size: 19px; }
  .banner-small .prize-note { left: 88px; top: 10px; font-size: 11px; }
  .banner-small .promo-title { left: 0; width: 199px; top: 28px; font-size: 44px; -webkit-text-stroke: 1px #0c0000; }
  .banner-small .tagline { left: 0; width: 199px; top: 86px; font-size: 11px; letter-spacing: .3px; }
  .banner-small .try-now { right: 0; bottom: 0; width: 76px; height: 24px; font-size: 11px; gap: 4px; }
  .banner-small .try-now svg { width: 7px; height: 9px; }

  /* 500 x 400 */
  .banner-rect { left: 99px; top: 284px; width: 500px; height: 400px; }
  .banner-rect .prize-amount { left: 124px; top: 20px; font-size: 35px; }
  .banner-rect .prize-note { left: 252px; top: 35px; font-size: 13px; }
  .banner-rect .promo-title { left: 0; width: 500px; top: 108px; font-size: 118px; }
  .banner-rect .tagline { left: 0; width: 500px; top: 236px; font-size: 20px; }
  .banner-rect .promo-dates { left: 195px; top: 357px; }
  .banner-rect .try-now { right: 0; bottom: 0; width: 130px; height: 35px; font-size: 16px; }

  /* 447 x 426 */
  .banner-square { left: 643px; top: 276px; width: 447px; height: 426px; }
  .banner-square .prize-amount { left: 90px; top: 24px; font-size: 35px; }
  .banner-square .prize-note { left: 226px; top: 36px; font-size: 13px; }
  .banner-square .promo-title { left: 0; width: 447px; top: 130px; font-size: 108px; }
  .banner-square .tagline { left: 0; width: 447px; top: 252px; font-size: 19px; }
  .banner-square .promo-dates { left: 164px; top: 380px; }
  .banner-square .try-now { right: 0; bottom: 0; width: 126px; height: 36px; font-size: 17px; }
</style>
</head>
<body>
  <svg width="0" height="0" style="position:absolute">
    <defs>
      <symbol id="chevron" viewBox="0 0 10 12"><path d="M2 0 L10 6 L2 12 L0 10 L5 6 L0 2 Z" fill="#fff"/></symbol>
    </defs>
  </svg>

  <section class="banner banner-leaderboard">
    <div class="banner-art" role="img" aria-label="Red light rays bursting from the centre with scattered glowing gems"></div>
    <div class="prize-amount">€10,000</div>
    <div class="prize-note">IN FREE ENTRIES</div>
    <div class="network-name"><span class="mark"></span>KRX</div>
    <h1 class="promo-title">Late Rush</h1>
    <p class="tagline">RUSH LATE, BAG A <strong>SEAT</strong></p>
    <div class="promo-dates">OCTOBER 1 – 31</div>
    <div class="try-now">Try Now <svg><use href="#chevron"/></svg></div>
  </section>

  <section class="banner banner-small">
    <div class="banner-art" role="img" aria-label="Red light rays bursting from the centre with scattered glowing gems"></div>
    <div class="prize-amount">€10,000</div>
    <div class="prize-note">IN FREE ENTRIES</div>
    <h1 class="promo-title">Late Rush</h1>
    <p class="tagline">RUSH LATE, BAG A <strong>SEAT</strong></p>
    <div class="try-now">Try Now <svg><use href="#chevron"/></svg></div>
  </section>

  <section class="banner banner-rect">
    <div class="banner-art" role="img" aria-label="Red light rays bursting from the centre with scattered glowing gems"></div>
    <div class="prize-amount">€10,000</div>
    <div class="prize-note">IN FREE ENTRIES</div>
    <h1 class="promo-title">Late Rush</h1>
    <p class="tagline">RUSH LATE, BAG A <strong>SEAT</strong></p>
    <div class="promo-dates">OCTOBER 1 – 31</div>
    <div class="try-now">Try Now <svg><use href="#chevron"/></svg></div>
  </section>

  <section class="banner banner-square">
    <div class="banner-art" role="img" aria-label="Red light rays bursting from the centre with scattered glowing gems"></div>
    <div class="prize-amount">€10,000</div>
    <div class="prize-note">IN FREE ENTRIES</div>
    <h1 class="promo-title">Late Rush</h1>
    <p class="tagline">RUSH LATE, BAG A <strong>SEAT</strong></p>
    <div class="promo-dates">OCTOBER 1 – 31</div>
    <div class="try-now">Try Now <svg><use href="#chevron"/></svg></div>
  </section>
</body>
</html>
```